Presentation Folder Saguaro Plan Advisors

I would like a two sided presentation folder 9" wide x 12" tall for our benefits/ insurance company. It must be professional and instill confidence in our customers. ArtHive designed our logo which must be included. Our website is www.spallc-example.org The logo on the website is the old one as a new website is about to launch. The contact information and address are correct on the website. We provide health, disability and other benefits to employers and will use this when making presentations about plans and renewals. I have been told to put this as stationery from someone at ArtHive but it is not stationery. Please feel free to email me if you have questions.

Reason: My committee meets Oct. 17.

```html
<!DOCTYPE html>
<html lang="en">
<head>
<meta charset="utf-8">
<title>Saguaro Plan Advisors – Presentation Folder</title>
<link href="https://fonts.googleapis.com/css2?family=Libre+Baskerville:wght@400&display=swap" rel="stylesheet">
<style>
  :root {
    --backdrop: #e2e2e2;
    --paper: #fafafa;
    --navy: #0f1270;
    --gold: #b98d2f;
  }
  * { margin: 0; padding: 0; box-sizing: border-box; }
  html, body {
    width: 1200px;
    height: 980px;
    overflow: hidden;
    background: var(--backdrop);
  }
  .folder-cover {
    position: absolute;
    left: 330px;
    top: 108px;
    width: 527px;
    height: 758px;
    background: var(--paper);
  }
  .brand-lockup {
    position: absolute;
    left: 172px;
    top: 188px;
    display: flex;
    align-items: center;
    gap: 14px;
  }
  .brand-mark {
    width: 34px;
    height: 34px;
    background: var(--navy);
    flex: none;
  }
  .brand-name {
    font-family: "Libre Baskerville", serif;
    font-weight: 400;
    font-size: 20px;
    line-height: 26px;
    color: var(--navy);
    white-space: nowrap;
  }
  .accent-band {
    position: absolute;
    left: 0;
    top: 319px;
    width: 100%;
    height: 12px;
    background: var(--gold);
  }
  .lower-panel {
    position: absolute;
    left: 0;
    top: 331px;
    width: 100%;
    bottom: 0;
    background: var(--navy);
  }
</style>
</head>
<body>
  <div class="folder-cover">
    <div class="brand-lockup">
      <div class="brand-mark"></div>
      <div class="brand-name">Saguaro Plan Advisors</div>
    </div>
    <div class="accent-band"></div>
    <div class="lower-panel"></div>
  </div>
</body>
</html>
```